First Aid Training business needs business card design

We would like a double sided business card designed for a first aid training business - Brindlewood First Aid. We provide first aid training and , WHS (work, health and safety) training.

The attached word document contains the key information we would like on each side of the business card.

Final design needs to be delivered in print ready format, along with the original file.

```html
<!DOCTYPE html>
<html lang="en">
<head>
<meta charset="utf-8">
<title>Brindlewood First Aid – Business Card</title>
<link rel="stylesheet" href="https://fonts.googleapis.com/css2?family=Arimo:wght@400;700&family=PT+Serif:wght@400;700&family=Roboto:wght@700&display=swap">
<style>
  :root {
    --page: #ffffff;
    --card: #ffffff;
    --card-edge: #ececec;
    --shadow: #e6e6e6;
    --red: #e92530;
    --ink: #111111;
    --white: #ffffff;
  }
  * { margin: 0; padding: 0; box-sizing: border-box; }
  html, body { width: 1200px; height: 1200px; overflow: hidden; background: var(--page); }
  .canvas { position: relative; width: 1200px; height: 1200px; }

  .card {
    position: absolute;
    left: 326px;
    width: 548px;
    height: 341px;
    background: var(--card);
    border: 1px solid var(--card-edge);
    box-shadow: 7px 7px 0 var(--shadow);
    overflow: hidden;
  }
  .card--front { top: 194px; }
  .card--back { top: 654px; }

  .brand {
    position: absolute;
    top: 30px;
    left: 104px;
    display: flex;
    align-items: center;
    gap: 32px;
  }
  .brand__mark {
    width: 100px;
    height: 100px;
    border-radius: 50%;
    background: var(--red);
    flex: none;
  }
  .brand__name {
    font-family: "Arimo", Arial, sans-serif;
    font-weight: 700;
    font-size: 27px;
    line-height: 1.12;
    letter-spacing: 0.5px;
    text-transform: uppercase;
    color: var(--ink);
  }

  .contact {
    position: absolute;
    left: 240px;
    top: 146px;
    font-family: "PT Serif", Georgia, serif;
    color: var(--ink);
  }
  .contact__name { font-weight: 700; font-size: 20px; line-height: 35px; }
  .contact__line { font-size: 19px; line-height: 35px; }

  .web-band {
    position: absolute;
    left: 0; right: 0; bottom: 0;
    height: 56px;
    background: var(--red);
    display: flex;
    align-items: center;
    justify-content: center;
    font-family: "Arimo", Arial, sans-serif;
    font-weight: 700;
    font-size: 25px;
    letter-spacing: 3px;
    color: var(--white);
  }

  .pitch {
    position: absolute;
    top: 160px;
    left: 0; right: 0;
    font-family: "Arimo", Arial, sans-serif;
    color: var(--ink);
  }
  .pitch__headline {
    text-align: center;
    font-weight: 700;
    font-size: 17px;
    letter-spacing: 2.2px;
    margin-left: 10px;
  }
  .benefits { list-style: none; margin: 6px 0 0 89px; }
  .benefits li {
    display: flex;
    align-items: center;
    gap: 6px;
    font-size: 17px;
    letter-spacing: 1.2px;
    line-height: 22px;
  }
  .benefits li::before {
    content: "";
    width: 68px;
    height: 9px;
    background: var(--red);
    flex: none;
  }
  .services {
    margin-top: 18px;
    text-align: center;
    font-family: "Roboto", Arial, sans-serif;
    font-weight: 700;
    font-size: 21px;
    line-height: 24px;
    margin-left: 12px;
  }
</style>
</head>
<body>
<main class="canvas">

  <section class="card card--front">
    <div class="brand">
      <span class="brand__mark"></span>
      <div class="brand__name">Brindlewood<br>First Aid</div>
    </div>
    <div class="contact">
      <p class="contact__name">Daniel Mercer</p>
      <p class="contact__line">0412 305 862</p>
      <p class="contact__line">help@brindlewoodfirstaid.com.au</p>
    </div>
    <div class="web-band">brindlewoodfirstaid.com.au</div>
  </section>

  <section class="card card--back">
    <div class="brand">
      <span class="brand__mark"></span>
      <div class="brand__name">Brindlewood<br>First Aid</div>
    </div>
    <div class="pitch">
      <p class="pitch__headline">Onsite Training - We can come to you</p>
      <ul class="benefits">
        <li>Time efficient</li>
        <li>Cost effective</li>
        <li>Minimise downtime for your team</li>
      </ul>
      <p class="services">First Aid Training<br>WHS Training</p>
    </div>
  </section>

</main>
</body>
</html>
```